Delivery Docket urgent plus require many other designs for more stationary after this.

We need a new delivery docket design urgently as the one we have needs updating and we have changed our company name. Please do not copy the one I have uploaded as we do not feel this looks professional enough. I uploaded it as a few designers requested to see what we are currently using thank you.
It is quite complex in that we need a range of information to be on the one docket.
We are a Transport Company based in Australia that has a wide variety of items that we deliver such as water, sand and gravels and heavy equipment transport.
We would prefer to keep this design to A5 size as we will get them made into books. We are looking for a modern professional look. Although it is only a delivery docket this is given to all our customers so needs to look impressive.

We need our new logo on the docket (PRW). There will also need to be areas for our address and contact numbers, email etc these will be supplied to the winning designer to make the final adjustments so for now just put something generic in these spaces.
Needs to have an area for customer details, purchase order number, date and docket number (docket number to be in red)
Needs a section where we can list the type of product / and or service that has been provided and the amount / qty usually 3 lines will be enough for this. Need area under this where the customer can sign name and print name to say that the goods / and or services have been received.

Also required somewhere on the docket are the words, Tax Invoice will be issued based on the information provided on this docket. Conditions on back of page

We then need a separate section on the same page which we will use internally that the staff member can tear off and hand into the office. On this section it needs to have area where the driver can list km at start of job and at end with space to calculate km travelled, details of fuel purchased eg amount and litres, vehicle that is being used. also need to log down wheel bearing temps.
prime mover needs spaces as follows
Steer axel FL____________ Steer axel FR _________ 1st drive axel L_______
1st drive axel R_________ 2nd drive axel L_______ 2nd drive axel R________

For the trailers need something similar x 2 as have 2 trailers
1st axel DS_________ 1st axel PS_________ 2nd axel DS__________
2nd axel PS_________ 3rd axel DS_________ 3rd axel PS__________

I have included a few examples of designs we have used in past and ones that we like so you can get an idea of the colours we prefer, I have included some of the designs we are currently receiving for our logo that I like so you can get idea again of colours we prefer. There is much more we need designed also such as time sheets, more delivery dockets and letter heads so there is a lot of more work available to the winning designer.

Thank you

Target Market(s)

Customers

Font styles to use
Serif
Sans Serif

Colors

Designer to choose colors to be used in the design.

Requirements
Should not have
• Please don't copy old docket as we do not like it and nned new info on new design thank you

```html
<!DOCTYPE html>
<html lang="en">
<head>
<meta charset="utf-8">
<title>PRW Delivery Docket</title>
<link rel="stylesheet" href="https://fonts.googleapis.com/css2?family=Source+Sans+3:wght@400;600;700&display=swap">
<style>
  :root {
    --stage-top: #1f1f1f;
    --stage-mid: #333333;
    --ink: #000000;
    --paper: #ffffff;
    --docket-red: #e0201b;
    --steel-dark: #3a3a3a;
    --steel-mid: #8a8a8a;
    --steel-light: #c9c9c9;
    --sky: #8f98a3;
    --earth: #a86a43;
  }
  * { box-sizing: border-box; margin: 0; padding: 0; }
  html, body { width: 1200px; height: 1200px; overflow: hidden; }
  body {
    position: relative;
    font-family: "Source Sans 3", "Myriad Pro", sans-serif;
    background: radial-gradient(ellipse at 50% 60%, var(--stage-mid) 0%, var(--stage-top) 75%);
    color: var(--ink);
  }
  .side-label {
    position: absolute;
    color: var(--paper);
    font-size: 42px;
    font-weight: 400;
    line-height: 1;
    transform: translateX(-50%);
  }
  .side-label--front { left: 253px; top: 196px; }
  .side-label--back { left: 824px; top: 312px; }

  /* Front cover */
  .cover {
    position: absolute;
    left: 34px; top: 262px;
    width: 440px; height: 677px;
    overflow: hidden;
  }
  .cover svg { position: absolute; inset: 0; }
  .cover-brand {
    position: absolute;
    left: 28px; top: 42px;
    font-size: 92px;
    font-weight: 700;
    letter-spacing: 2px;
    color: #1c1c1c;
    line-height: 1;
  }

  /* Back form */
  .docket {
    position: absolute;
    left: 495px; top: 382px;
    width: 675px; height: 436px;
    background: var(--paper);
    font-size: 7px;
  }
  .docket-brand {
    position: absolute;
    left: 0; right: 0; top: 12px;
    text-align: center;
    font-size: 52px;
    font-weight: 700;
    letter-spacing: 2px;
    line-height: 1;
    color: #1c1c1c;
  }
  .contact-band {
    position: absolute;
    left: 0; right: 0; top: 72px; height: 16px;
    background: var(--ink);
    color: var(--paper);
    font-size: 8.5px;
  }
  .contact-item {
    position: absolute;
    top: 0; height: 16px;
    display: flex; align-items: center; gap: 4px;
  }
  .contact-item svg { width: 10px; height: 10px; }

  .field {
    position: absolute;
    height: 12px;
    border: 1px solid #555;
    padding-left: 7px;
    display: flex; align-items: center;
    font-size: 6.6px;
  }
  .field--heading {
    background: var(--ink);
    color: var(--paper);
    justify-content: center;
    padding: 0;
    border-color: var(--ink);
  }
  .docket-number {
    color: var(--docket-red);
    font-size: 10px;
    margin-left: auto;
    margin-right: 18px;
  }

  .items {
    position: absolute;
    left: 11px; top: 143px;
    width: 652px;
    border-collapse: collapse;
    border: 1.5px solid var(--ink);
  }
  .items th {
    background: var(--ink);
    color: var(--paper);
    font-weight: 400;
    font-size: 10px;
    height: 21px;
  }
  .items th + th { border-left: 1.5px solid var(--paper); }
  .items td {
    border: 1.2px solid var(--ink);
    height: 19.5px;
  }
  .items .qty-col { width: 102px; }
  .items tr.note-row td { height: 28px; }
  .invoice-note {
    text-align: center;
    font-size: 6.6px;
    line-height: 1.6;
  }

  .tear-line {
    position: absolute;
    left: 0; right: 0; top: 280px;
    border-top: 1.2px dashed var(--ink);
  }

  .receipt {
    position: absolute;
    left: 11px; top: 289px;
    width: 382px; height: 68px;
    border: 1.2px solid var(--ink);
    display: grid;
    grid-template-columns: 191px 1fr;
    grid-template-rows: 22px 1fr;
  }
  .receipt-head {
    background: var(--ink);
    color: var(--paper);
    font-size: 10px;
    display: flex; align-items: center; justify-content: center;
  }
  .receipt-head + .receipt-head { border-left: 2px solid var(--paper); }
  .receipt-cell + .receipt-cell { border-left: 1.2px solid var(--ink); }

  .log-box {
    position: absolute;
    border: 1.5px solid var(--ink);
  }
  .log-row {
    height: 50%;
    display: flex; align-items: center;
    padding-left: 6px;
    font-size: 6.6px;
  }
  .log-row + .log-row { border-top: 1.2px solid var(--ink); }

  .axle-box {
    position: absolute;
    top: 364px; height: 64px; width: 321px;
    border: 1.2px solid var(--ink);
  }
  .axle-title {
    position: absolute;
    left: 50%; top: 0;
    transform: translateX(-50%);
    width: 154px; height: 12px;
    background: var(--ink);
    color: var(--paper);
    font-size: 7.5px;
    display: flex; align-items: center; justify-content: center;
  }
  .axle-line {
    position: absolute;
    left: 0; right: 0;
    text-align: center;
    font-size: 7.5px;
    white-space: pre;
  }
</style>
</head>
<body>

<div class="side-label side-label--front">Front</div>
<div class="side-label side-label--back">Back</div>

<section class="cover">
  <svg width="440" height="677" viewBox="0 0 440 677">
    <defs>
      <linearGradient id="steelGrad" x1="0" y1="0" x2="1" y2="1">
        <stop offset="0" stop-color="#4a4a4a"/>
        <stop offset="1" stop-color="#7a7a7a"/>
      </linearGradient>
      <linearGradient id="truckArtGrad" x1="0" y1="0" x2="1" y2="1">
        <stop offset="0" stop-color="#d6d6d6"/>
        <stop offset="0.5" stop-color="#6c6c6c"/>
        <stop offset="1" stop-color="#a8a8a8"/>
      </linearGradient>
      <linearGradient id="siteGrad" x1="0" y1="0" x2="0" y2="1">
        <stop offset="0" stop-color="#9aa2ab"/>
        <stop offset="0.55" stop-color="#6e6a64"/>
        <stop offset="0.7" stop-color="#9b6846"/>
        <stop offset="1" stop-color="#b27550"/>
      </linearGradient>
    </defs>
    <rect width="440" height="677" fill="url(#steelGrad)" role="img" aria-label="Brushed dark steel texture"/>
    <polygon points="0,678 0,442 234,562 440,402 440,678" fill="url(#siteGrad)" role="img" aria-label="Photo of a road train with side tipper trailers on a red dirt outback track"/>
    <polygon points="0,154 142,206 440,82 440,402 234,562 0,378" fill="url(#truckArtGrad)" role="img" aria-label="Stylised monochrome illustration of two prime mover trucks over checker plate"/>
  </svg>
  <div class="cover-brand">PRW</div>
</section>

<section class="docket">
  <div class="docket-brand">PRW</div>

  <div class="contact-band">
    <div class="contact-item" style="left:139px">
      <svg viewBox="0 0 10 10"><circle cx="5" cy="5" r="4.5" fill="none" stroke="#fff" stroke-width="0.8"/><path d="M5 2.4a1.7 1.7 0 0 1 1.7 1.7c0 1.3-1.7 3.3-1.7 3.3S3.3 5.4 3.3 4.1A1.7 1.7 0 0 1 5 2.4z" fill="#fff"/></svg>
      <span>Address:</span>
    </div>
    <div class="contact-item" style="left:313px">
      <svg viewBox="0 0 10 10"><circle cx="5" cy="5" r="4.5" fill="none" stroke="#fff" stroke-width="0.8"/><path d="M3.2 2.6l1 1-.5.7a3.5 3.5 0 0 0 2 2l.7-.5 1 1-.7.8C5 7.6 2.4 5 2.4 3.3z" fill="#fff"/></svg>
      <span>123 456 7890</span>
    </div>
    <div class="contact-item" style="left:390px">
      <svg viewBox="0 0 10 10"><circle cx="5" cy="5" r="4.5" fill="#fff"/><rect x="2.6" y="3.3" width="4.8" height="3.4" fill="#000"/><path d="M2.6 3.3L5 5.2l2.4-1.9" fill="none" stroke="#fff" stroke-width="0.5"/></svg>
      <span>info@prw.com</span>
    </div>
    <div class="contact-item" style="left:469px">
      <svg viewBox="0 0 10 10"><circle cx="5" cy="5" r="4.3" fill="none" stroke="#fff" stroke-width="0.8"/><ellipse cx="5" cy="5" rx="1.8" ry="4.3" fill="none" stroke="#fff" stroke-width="0.6"/><path d="M0.7 5h8.6M1.5 3h7M1.5 7h7" stroke="#fff" stroke-width="0.5"/></svg>
      <span>www.prw.com</span>
    </div>
  </div>

  <div class="field field--heading" style="left:11px; top:94px; width:158px;">Customer Details</div>
  <div class="field" style="left:182px; top:94px; width:148px;">Delivery Docket: <span class="docket-number">2050</span></div>
  <div class="field" style="left:343px; top:94px; width:159px;">Purchase Order Number:</div>
  <div class="field" style="left:514px; top:94px; width:149px;"></div>

  <div class="field" style="left:11px; top:110px; width:158px;">Name:</div>
  <div class="field" style="left:182px; top:110px; width:148px;">Date:</div>
  <div class="field" style="left:343px; top:110px; width:159px;">Contact:</div>
  <div class="field" style="left:514px; top:110px; width:149px;">Phone:</div>

  <div class="field" style="left:11px; top:125px; width:652px; height:13px;">Billing Address:</div>

  <table class="items">
    <thead>
      <tr><th class="qty-col">Qty</th><th>Description</th></tr>
    </thead>
    <tbody>
      <tr><td></td><td></td></tr>
      <tr><td></td><td></td></tr>
      <tr><td></td><td></td></tr>
      <tr><td></td><td></td></tr>
      <tr class="note-row"><td></td><td class="invoice-note">This Invoice will be based on information provided on this docket.<br>Conditions on back of page.</td></tr>
    </tbody>
  </table>

  <div class="tear-line"></div>

  <div class="receipt">
    <div class="receipt-head">Good Received by (Print Name)</div>
    <div class="receipt-head">Signed:</div>
    <div class="receipt-cell"></div>
    <div class="receipt-cell"></div>
  </div>

  <div class="log-box" style="left:406px; top:289px; width:124px; height:32px;">
    <div class="log-row">Start of Job:</div>
    <div class="log-row">Fuel Amount:</div>
  </div>
  <div class="log-box" style="left:540px; top:289px; width:123px; height:32px;">
    <div class="log-row">End of Job:</div>
    <div class="log-row">Vehical:</div>
  </div>
  <div class="log-box" style="left:485px; top:326px; width:123px; height:32px;">
    <div class="log-row">Total KM Traveled:</div>
    <div class="log-row">Wheel Temps:</div>
  </div>

  <div class="axle-box" style="left:11px;">
    <div class="axle-title">Prime Mover</div>
    <div class="axle-line" style="top:28px;">Steer axel FL____________ Steer axel FR _________ 1st drive axel L_______</div>
    <div class="axle-line" style="top:47px;">1st drive axel R_________ 2nd drive axel L_______ 2nd drive axel R________</div>
  </div>
  <div class="axle-box" style="left:342px;">
    <div class="axle-title">For The Trailers</div>
    <div class="axle-line" style="top:28px;">1st axel DS_________ 1st axel PS_________ 2nd axel DS__________</div>
    <div class="axle-line" style="top:47px;">2nd axel PS_________ 3rd axel DS_________ 3rd axel PS__________</div>
  </div>
</section>

</body>
</html>
```